Review/Re-Design Supermarket E-Commerce website

We have launched our Supermarket E-commerce Website but feel it is lacking a modern feel.

Please re-design the current Supermarket E-commerce site, creating a more modern look and feel.

I am looking for design changes to things such as:

- Fonts
- Button shape & Size
- Shapes of boxes
- Layout of drop down menus
- A new shopping cart / button
- The Header (and in particular the use and positioning of the logo)
- Supplying a generic background image (currently berries)

Please do not change the structure of the page. For instance, the category selection will always be on the left, the items will always be displayed in rows of 3 and the shopping cart should be on the right.
Updates

Current site can be found at www.brovanmarket.com.au

Project Deadline Extended
Reason: designs coming in are generally too different from current design. we are looking for less that 10% change to the overall look and feel. one aspect that needs a lot of work is the checkout cart on the right hand side. please checkout http://www2.pelkinfreshmart.com.au/?gclid=QXRP4kdmwnLBHTYEzJuaPGEKtB

Target Market(s)

Consumers buying their weekly grocery shopping online

Industry/Entity Type

Shopping

Number of Pages Required

1 page

Requirements
Must have
• Stick to the branding of the Logo. Which is Red, Blue and White.
• Other colours may be used in small percentages.
Should not have
• Do not change the Structure of the site.

```html
<!DOCTYPE html>
<html lang="en">
<head>
<meta charset="utf-8">
<title>Brovan Market – Apples</title>
<link href="https://fonts.googleapis.com/css2?family=Questrial&family=Open+Sans:wght@700&display=swap" rel="stylesheet">
<style>
:root{
  --page-bg:#efefef;
  --sheet:#ffffff;
  --brand-blue:#1e5ba8;
  --bar-blue:#7fa7d2;
  --search-btn:#1a5aa3;
  --tag-blue:#86acd6;
  --card-bg:#efeeec;
  --price:#e98089;
  --red:#e3342f;
  --ink:#333333;
  --line:#555555;
  --kraft:#b89a78;
  --kraft-light:#c9ad8c;
  --kraft-edge:#ad8f6d;
  --go-green:#6f9f80;
  --tick-green:#6a9879;
  --qty:#c9c9c9;
}
*{box-sizing:border-box;margin:0;padding:0}
html,body{width:1200px;height:842px;overflow:hidden}
body{background:var(--page-bg);font-family:'Questrial',sans-serif;color:var(--ink);position:relative}
.backdrop{position:absolute;inset:0;background:linear-gradient(180deg,#f2f2f2,#ebebeb)}
.sheet{position:absolute;left:100px;top:0;width:1027px;height:842px;background:var(--sheet)}
.header{position:absolute;left:100px;top:0;width:1027px;height:120px;background:#f6f6f6}
.brand{position:absolute;left:162px;top:36px;display:flex;align-items:center;gap:12px}
.brand-name{font-size:32px;line-height:36px;color:var(--brand-blue);letter-spacing:2px}
.brand-dot{width:22px;height:22px;border-radius:50%;background:var(--red)}
.nav-bag{position:absolute;background:var(--kraft-light);color:#fff;font-size:15px;line-height:18px;padding:6px 14px;border-left:1px solid var(--kraft-edge);box-shadow:-3px 0 4px rgba(0,0,0,.12)}
.toolbar{position:absolute;left:100px;top:120px;width:1027px;height:48px;background:var(--bar-blue)}
.phone{position:absolute;left:160px;top:133px;color:#fff;font-size:16px;line-height:20px;display:flex;align-items:center;gap:6px}
.search{position:absolute;left:347px;top:129px;width:195px;height:27px;background:#fff;color:#999;font-size:16px;line-height:27px;padding:0 7px}
.search-btn{position:absolute;left:542px;top:129px;width:64px;height:27px;background:var(--search-btn);display:flex;align-items:center;justify-content:center}
.select{position:absolute;top:129px;height:27px;background:#fff;color:var(--brand-blue);font-size:16px;display:flex;align-items:center;justify-content:space-between;padding:0 14px 0 0}
.select span{flex:1;text-align:center}
.filter{left:620px;width:122px}
.sort{left:757px;width:122px}
.categories{position:absolute;left:151px;top:194px;width:152px;list-style:none}
.categories li{height:33px;border-bottom:1px solid var(--line);font-size:13px;display:flex;align-items:center;padding-left:15px}
.categories .fav{color:var(--brand-blue);font-weight:700;font-family:'Open Sans',sans-serif;font-size:12px;height:34px;padding-left:12px;gap:6px}
.categories .special{color:var(--red);font-weight:700;font-family:'Open Sans',sans-serif;font-size:12px;height:36px;padding-left:12px;gap:6px}
.categories .active{background:var(--tag-blue)}
.categories .sub{padding-left:40px}
.crumbs{position:absolute;left:340px;top:190px;font-size:13px}
.crumbs a{color:var(--red);text-decoration:none}
.product{position:absolute;width:168px;height:296px;background:var(--card-bg)}
.product-title{height:34px;background:var(--tag-blue);color:#fff;font-family:'Open Sans',sans-serif;font-weight:700;font-size:11px;white-space:nowrap;display:flex;align-items:center;justify-content:center}
.product-photo{position:absolute;left:9px;top:41px;width:150px;height:122px;overflow:hidden}
.photo-red{background:radial-gradient(circle,#d42a34 0%,#c4212b 45%,#fbfbfb 70%)}
.photo-fuji{background:radial-gradient(circle,#c2484b 0%,#b33a3f 35%,#fdfdfd 48%)}
.photo-green{background:radial-gradient(circle,#6ecb2c 0%,#4ea61f 35%,#fdfdfd 48%)}
.photo-rose{background:radial-gradient(circle,#d72a3f 0%,#c41f33 35%,#fdfdfd 48%)}
.photo-gala{background:radial-gradient(circle,#e8a040 0%,#d4623a 35%,#fdfdfd 48%)}
.photo-yellow{background:radial-gradient(circle,#c6dc4c 0%,#a8c431 45%,#fbfbfb 70%)}
.pick-tick{position:absolute;right:0;bottom:0}
.price{position:absolute;left:58px;top:170px;width:52px;height:52px;border-radius:50%;background:var(--price);color:#fff;text-align:center;padding-top:12px}
.price b{display:block;font-weight:400;font-size:17px;line-height:17px}
.price small{display:block;font-size:7px;line-height:9px}
.qty{position:absolute;left:0;right:0;top:228px;display:flex;justify-content:center;align-items:center;gap:8px;font-size:16px}
.qty i{width:12px;height:12px;border-radius:50%;background:var(--qty);color:#fff;font-style:normal;font-size:11px;line-height:12px;text-align:center}
.add{position:absolute;left:30px;top:252px;width:106px;height:33px;background:var(--tag-blue);color:#fff;font-size:16px;display:flex;align-items:center;justify-content:center}
.cart{position:absolute;left:913px;top:228px;width:177px;height:294px;background:linear-gradient(180deg,var(--kraft-light),var(--kraft));clip-path:polygon(2% 0,98% 2%,100% 96%,10% 100%,3% 60%)}
.cart-line{position:absolute;left:932px;color:#fff;display:flex;gap:8px;align-items:flex-start}
.cart-line strong{font-size:12px;line-height:14px;font-weight:400;display:block}
.cart-line small{font-size:7px;display:block;line-height:8px}
.cart-rule{position:absolute;left:926px;top:341px;width:135px;height:1px;background:#fff}
.cart-total{position:absolute;left:932px;top:364px;color:#fff;display:flex;align-items:center;width:120px;justify-content:space-between}
.cart-total div{text-align:right;font-size:7px;line-height:9px}
.cart-total b{font-size:15px;display:block;line-height:18px}
.checkout{position:absolute;left:925px;top:428px;width:135px;height:33px;background:var(--go-green);color:#fff;font-size:16px;display:flex;align-items:center;justify-content:center}
.to-top{position:absolute;left:29px;top:780px}
</style>
</head>
<body>
<div class="backdrop" role="img" aria-label="Light grey background of line-drawn vegetables"></div>
<div class="sheet"></div>

<header class="header"></header>
<div class="brand"><span class="brand-name">BROVAN MARKET</span><span class="brand-dot"></span></div>
<div class="nav-bag" style="left:593px;top:32px;width:160px;height:88px">Products</div>
<div class="nav-bag" style="left:672px;top:60px;width:108px;height:60px;padding-top:6px">Login</div>
<div class="nav-bag" style="left:778px;top:32px;width:160px;height:88px">Register</div>
<div class="nav-bag" style="left:855px;top:60px;width:100px;height:60px">Products</div>
<div class="nav-bag" style="left:955px;top:22px;width:170px;height:98px">My Cart</div>

<div class="toolbar"></div>
<div class="phone">
  <svg width="16" height="16" viewBox="0 0 24 24"><path fill="#fff" d="M6.6 10.8a15 15 0 0 0 6.6 6.6l2.2-2.2c.3-.3.7-.4 1-.2 1.1.4 2.3.6 3.6.6.6 0 1 .4 1 1V20c0 .6-.4 1-1 1A17 17 0 0 1 3 4c0-.6.4-1 1-1h3.5c.6 0 1 .4 1 1 0 1.3.2 2.5.6 3.6.1.3 0 .7-.2 1z"/></svg>
  1300 542 918
</div>
<div class="search">Search...</div>
<div class="search-btn"><svg width="20" height="20" viewBox="0 0 20 20"><circle cx="8" cy="8" r="6" fill="none" stroke="#fff" stroke-width="2.4"/><path d="M12.5 12.5 18 18" stroke="#fff" stroke-width="2.6" stroke-linecap="round"/></svg></div>
<div class="select filter"><span>Filter by</span><svg width="12" height="8"><path d="M0 0h12L6 7z" fill="#1e5ba8"/></svg></div>
<div class="select sort"><span>Sort</span><svg width="12" height="8"><path d="M0 0h12L6 7z" fill="#1e5ba8"/></svg></div>

<ul class="categories">
  <li class="fav"><svg width="24" height="22" viewBox="0 0 24 22"><path d="M12 0l3 7.5 8 .5-6 5 2 8-7-4.5L5 21l2-8-6-5 8-.5z" fill="#1e7d4a"/></svg>Favourites</li>
  <li class="special"><svg width="20" height="20"><circle cx="10" cy="10" r="10" fill="#e3342f"/><text x="10" y="15" font-size="14" fill="#fff" text-anchor="middle" font-family="Open Sans" font-weight="700">$</text></svg>Online Specials</li>
  <li>Fruit</li><li>Vegetables</li><li>Meat</li><li>Servicsed Deli</li><li>Bakery</li>
  <li>Chilled Food</li><li>Frozen Food</li><li>Milk</li><li>Baby</li>
  <li></li>
  <li>Baking Needs</li><li>Beverages</li><li>Biscuites</li>
  <li class="active">Breakfast Food</li>
  <li class="sub">Cereal</li><li class="sub">Drinks</li><li class="sub">Muesli</li>
</ul>

<nav class="crumbs"><a href="#">Home</a> / Fruit / Apples</nav>

<article class="product" style="left:340px;top:224px">
  <h2 class="product-title">APPLES RED 2KG BAG</h2>
  <div class="product-photo photo-red" role="img" aria-label="Bunch of red apples"></div>
  <div class="price"><b>$8.39</b><small>$8.39ea</small></div>
  <div class="qty"><i>−</i>1<i>+</i></div>
  <div class="add">ADD</div>
</article>
<article class="product" style="left:528px;top:224px">
  <h2 class="product-title">FUJI APPLES EACH</h2>
  <div class="product-photo photo-fuji" role="img" aria-label="Single red-striped apple">
    <svg class="pick-tick" width="52" height="52"><path d="M52 0v52H0z" fill="#6a9879"/><circle cx="34" cy="34" r="7" fill="none" stroke="#fff" stroke-width="1.6"/><path d="M30.5 34l2.5 2.5 4.5-5" fill="none" stroke="#fff" stroke-width="1.8"/></svg>
  </div>
  <div class="price"><b>$0.60</b><small>$0.60ea</small></div>
  <div class="qty"><i>−</i>1<i>+</i></div>
  <div class="add">ADD</div>
</article>
<article class="product" style="left:717px;top:224px">
  <h2 class="product-title">GREEN APPLES EACH</h2>
  <div class="product-photo photo-green" role="img" aria-label="Single green apple with leaf"></div>
  <div class="price"><b>$0.60</b><small>$0.60ea</small></div>
  <div class="qty"><i>−</i>1<i>+</i></div>
  <div class="add">ADD</div>
</article>
<article class="product" style="left:340px;top:538px">
  <h2 class="product-title">ROSE BLUSH APPLES EACH</h2>
  <div class="product-photo photo-rose" role="img" aria-label="Single deep pink apple">
    <svg class="pick-tick" width="52" height="52"><path d="M52 0v52H0z" fill="#6a9879"/><circle cx="34" cy="34" r="7" fill="none" stroke="#fff" stroke-width="1.6"/><path d="M30.5 34l2.5 2.5 4.5-5" fill="none" stroke="#fff" stroke-width="1.8"/></svg>
  </div>
  <div class="price"><b>$0.60</b><small>$0.60ea</small></div>
  <div class="qty"><i>−</i>1<i>+</i></div>
  <div class="add">ADD</div>
</article>
<article class="product" style="left:528px;top:538px">
  <h2 class="product-title">ROYAL GALA APPLES EACH</h2>
  <div class="product-photo photo-gala" role="img" aria-label="Single red and yellow apple"></div>
  <div class="price"><b>$0.60</b><small>$0.60ea</small></div>
  <div class="qty"><i>−</i>1<i>+</i></div>
  <div class="add">ADD</div>
</article>
<article class="product" style="left:717px;top:538px">
  <h2 class="product-title">YELLOW APPLES 1.5KG BAG</h2>
  <div class="product-photo photo-yellow" role="img" aria-label="Pile of yellow apples with slices"></div>
  <div class="price"><b>$5.20</b><small>$5.20ea</small></div>
  <div class="qty"><i>−</i>1<i>+</i></div>
  <div class="add">ADD</div>
</article>

<aside>
  <div class="cart" role="img" aria-label="Brown paper shopping bag"></div>
  <div class="cart-line" style="top:282px">
    <svg width="18" height="24" viewBox="0 0 18 24"><path d="M5 9V6a4 4 0 0 1 8 0v3" fill="none" stroke="#fff" stroke-width="2"/><rect x="1" y="9" width="16" height="14" fill="#fff"/></svg>
    <div><strong>CLICK&amp;COLLECT</strong><small>4/12-18 Marlow Street<br>Kelby TAS 7390</small></div>
  </div>
  <div class="cart-line" style="top:319px">
    <svg width="22" height="14" viewBox="0 0 22 14"><rect x="0" y="1" width="13" height="9" fill="#fff"/><path d="M13 4h5l3 3v3h-8z" fill="#fff"/><circle cx="4" cy="12" r="2" fill="#fff"/><circle cx="17" cy="12" r="2" fill="#fff"/></svg>
    <div><strong>DELIVERY INFO</strong></div>
  </div>
  <div class="cart-rule"></div>
  <div class="cart-total">
    <svg width="46" height="40" viewBox="0 0 46 40"><path d="M0 4h8l6 22h24l5-16H12" fill="none" stroke="#fff" stroke-width="4"/><circle cx="16" cy="35" r="4" fill="#fff"/><circle cx="35" cy="35" r="4" fill="#fff"/><path d="M20 16l5 4 9-9" fill="none" stroke="#fff" stroke-width="3"/></svg>
    <div>3 items<br>Sub Total<b>$0.60</b></div>
  </div>
  <div class="checkout">CHECKOUT</div>
</aside>

<svg class="to-top" width="46" height="46" viewBox="0 0 46 46"><path d="M23 0 46 23 23 46 0 23z" fill="#8fb59a" opacity=".7"/><circle cx="23" cy="23" r="10" fill="none" stroke="#fff" stroke-width="2"/><path d="M23 29V17m-5 5 5-5 5 5" fill="none" stroke="#fff" stroke-width="2.2"/></svg>
</body>
</html>
```